Business Card

We are looking to re-create our business card. Attached is the company logo. we would like it to be back and front. for example one side with the persons information and the other side with the company logo. Be as creative as you would like but also keep in mind, we are a Health Insurance company and we need to look professional as well.
Industry/Entity Type
Business

```html
<!DOCTYPE html>
<html lang="en">
<head>
<meta charset="utf-8">
<title>Crestline Health Cover – Business Card</title>
<link rel="stylesheet" href="https://fonts.googleapis.com/css2?family=Didact+Gothic&family=Source+Sans+3:wght@400&display=swap">
<style>
  :root {
    --backdrop: #b4b5b5;
    --brand-blue: #0a86c2;
    --paper: #ffffff;
    --ink-blue: #1186c4;
    --card-shadow: rgba(0, 0, 0, 0.22);
  }
  html, body {
    margin: 0;
    padding: 0;
    width: 1200px;
    height: 918px;
    overflow: hidden;
    background: var(--backdrop);
  }
  .canvas {
    position: relative;
    width: 1200px;
    height: 918px;
  }
  .card {
    position: absolute;
    left: 330px;
    width: 540px;
    height: 309px;
    background: var(--paper);
    box-shadow: 0 8px 24px var(--card-shadow);
    overflow: hidden;
  }
  .card--contact { top: 105px; }
  .card--brand { top: 494px; }

  /* Contact side */
  .contact-details {
    position: absolute;
    left: 36px;
    top: 42px;
    font-family: "Didact Gothic", sans-serif;
    color: var(--ink-blue);
  }
  .contact-name {
    margin: 0 0 10px;
    font-size: 27px;
    font-weight: 400;
    letter-spacing: 0.3px;
  }
  .contact-line {
    margin: 0;
    font-size: 15px;
    line-height: 1.3;
  }
  .contact-label { font-style: italic; }
  .contact-band {
    position: absolute;
    right: 0;
    top: 0;
    width: 142px;
    height: 100%;
    background: var(--brand-blue);
  }
  .contact-band .brand-lockup {
    position: absolute;
    left: 12px;
    top: 18px;
    transform: scale(0.32);
    transform-origin: left top;
  }

  /* Brand side */
  .brand-panel {
    position: absolute;
    left: 0;
    top: 0;
    width: 412px;
    height: 100%;
    background: var(--brand-blue);
  }
  .brand-panel .brand-lockup {
    position: absolute;
    left: 48px;
    top: 122px;
  }

  /* Lockup shared */
  .brand-lockup {
    display: flex;
    align-items: center;
    font-family: "Source Sans 3", sans-serif;
    font-weight: 400;
    color: var(--paper);
    white-space: nowrap;
  }
  .brand-square {
    width: 12px;
    height: 12px;
    background: var(--paper);
    margin-right: 8px;
  }
  .brand-initials {
    font-size: 38px;
    letter-spacing: 0.5px;
  }
  .brand-rule {
    width: 1px;
    height: 62px;
    background: var(--paper);
    margin: 0 12px 0 14px;
  }
  .brand-name {
    font-size: 25px;
    padding-top: 22px;
  }
</style>
</head>
<body>
<main class="canvas">

  <section class="card card--contact" aria-label="Business card, contact side">
    <div class="contact-details">
      <h1 class="contact-name">Name Here</h1>
      <p class="contact-line"><span class="contact-label">phone:</span> +61 (0) 400 555 019</p>
      <p class="contact-line"><span class="contact-label">email:</span> hello@crestlinecover.com</p>
    </div>
    <div class="contact-band">
      <div class="brand-lockup">
        <span class="brand-square"></span>
        <span class="brand-initials">CHC</span>
        <span class="brand-rule"></span>
        <span class="brand-name">Crestline Health Cover</span>
      </div>
    </div>
  </section>

  <section class="card card--brand" aria-label="Business card, brand side">
    <div class="brand-panel">
      <div class="brand-lockup">
        <span class="brand-square"></span>
        <span class="brand-initials">CHC</span>
        <span class="brand-rule"></span>
        <span class="brand-name">Crestline Health Cover</span>
      </div>
    </div>
  </section>

</main>
</body>
</html>
```